Commercial cleaning business needs a trifold brochure to spotlight janitorial services offered.

Looking for a catchy, creative, trifold brochure to give a description of services offered. This would be used for new potential customers. Our primary colors are royal blue, light gray, and white as included in our logo. The logo does include "restoration", however we only want this brochure to be focused solely on the commercial cleaning side for janitorial services as we already purchased a brochure for the restoration. You can visit our website to get a better idea. www.tvrqservices.example

```html
<!DOCTYPE html>
<html lang="en">
<head>
<meta charset="utf-8">
<title>Bluegrass Summit Building Care – Trifold Brochure</title>
<link rel="stylesheet" href="https://fonts.googleapis.com/css2?family=Oswald:wght@400;500;700&family=Open+Sans:wght@400;600;700&display=swap">
<style>
  :root{
    --royal:#2e2a86;
    --royal-deep:#232070;
    --lavender:#7c79c2;
    --panel-light:#eeeff2;
    --panel-white:#f7f7f9;
    --ink:#1d1d24;
    --ink-soft:#3a3a44;
    --white:#ffffff;
    --page-bg:#d9dade;
    --photo-a:#c9d6e3;
    --photo-b:#8fa9c4;
  }
  *{box-sizing:border-box;margin:0;padding:0}
  html,body{width:1200px;height:800px;overflow:hidden;background:var(--page-bg)}
  .brochure{position:absolute;left:30px;top:20px;width:1140px;height:760px;display:flex;box-shadow:0 6px 24px rgba(0,0,0,.18);overflow:hidden}
  .panel{position:relative;width:380px;height:760px}
  .panel--efficiency{background:linear-gradient(180deg,var(--panel-white),var(--panel-light))}
  .panel--services{background:var(--royal)}
  .panel--vision{background:linear-gradient(160deg,var(--panel-white),var(--panel-light))}

  .heading{font-family:'Oswald',sans-serif;text-transform:uppercase;line-height:1.08;white-space:nowrap}
  .heading__light{font-weight:400;color:var(--ink)}
  .heading__bold{font-weight:700;color:var(--royal)}
  .rule{height:2px;background:var(--royal);margin-top:8px}
  .body{font-family:'Open Sans',sans-serif;font-size:12.5px;line-height:1.55;color:var(--ink-soft);text-align:justify}

  /* panel 1 */
  .efficiency__column{position:absolute;left:40px;top:55px;width:305px;z-index:1}
  .efficiency__head .heading__light{font-size:28px}
  .efficiency__head .heading__bold{font-size:30px}
  .efficiency__text{margin-top:18px}
  .efficiency__text p+p{margin-top:14px}
  .office-photo{position:absolute;left:0;top:0}

  /* panel 2 */
  .services__head{position:absolute;left:30px;top:45px;width:320px}
  .services__head .heading{font-size:34px;color:var(--white)}
  .services__head .heading b{font-weight:700}
  .services__head .heading span{font-weight:400}
  .services__head .rule{background:var(--white)}
  .services__intro{position:absolute;left:30px;top:112px;width:320px;font-family:'Open Sans',sans-serif;font-size:14px;line-height:1.5;color:var(--white)}
  .service-list{position:absolute;left:30px;top:192px;width:330px;list-style:none}
  .service-list li{display:flex;gap:10px;font-family:'Open Sans',sans-serif;font-size:13.5px;line-height:1.35;color:var(--white);margin-bottom:7px}
  .service-list strong{font-weight:700;text-transform:uppercase}
  .service-list svg{flex:none;margin-top:2px}
  .call-banner{position:absolute;left:30px;top:648px;width:320px;text-align:center}
  .call-banner__label{display:inline-block;background:var(--white);color:var(--royal);font-family:'Oswald',sans-serif;font-size:24px;padding:2px 18px;border-radius:4px;text-transform:uppercase}
  .call-banner__label b{font-weight:700}
  .call-banner__phone{font-family:'Oswald',sans-serif;font-weight:700;font-size:42px;line-height:1.2;color:var(--white);letter-spacing:1px;margin-top:2px}

  /* photo circles across fold */
  .photo-circle{position:absolute;border-radius:50%;border:5px solid var(--white);box-shadow:0 0 0 2px var(--royal-deep)}
  .photo-circle--team{left:335px;top:395px;width:240px;height:240px;background:radial-gradient(circle at 45% 40%,var(--photo-a),var(--photo-b))}
  .photo-circle--supplies{left:565px;top:410px;width:205px;height:205px;background:radial-gradient(circle at 50% 55%,#9cc4e4,#5a5f78)}
  .bubble{position:absolute;border-radius:50%}
  .bubble--lav{background:var(--lavender)}
  .bubble--pale{background:rgba(200,200,235,.55)}

  /* panel 3 */
  .vision__head{position:absolute;left:40px;top:40px;width:310px}
  .vision__head .heading__light,.values__head .heading__light{font-size:32px}
  .vision__head .heading__bold,.values__head .heading__bold{font-size:32px}
  .vision__text{position:absolute;left:40px;top:100px;width:305px;font-size:11.5px}
  .vision__text p+p{margin-top:12px}
  .values__head{position:absolute;left:40px;top:345px;width:310px}
  .value-list{position:absolute;left:40px;top:410px;width:320px;list-style:none}
  .value{display:flex;align-items:center;height:84px}
  .value__icon{flex:none;width:62px;height:62px;border-radius:50%;border:2px solid var(--royal);background:var(--white);display:flex;align-items:center;justify-content:center;box-shadow:4px 6px 10px rgba(0,0,0,.12)}
  .value__divider{flex:none;width:1px;height:54px;background:#b9b9c4;margin:0 14px}
  .value__title{font-family:'Open Sans',sans-serif;font-weight:700;font-size:16px;color:var(--royal)}
  .value__text{font-family:'Open Sans',sans-serif;font-size:11.5px;line-height:1.35;color:var(--ink-soft)}
</style>
</head>
<body>
<main class="brochure">

  <section class="panel panel--efficiency">
    <svg class="office-photo" width="380" height="760" viewBox="0 0 380 760" role="img" aria-label="Photo of two cleaners in blue aprons wiping desks in a bright modern office">
      <defs><linearGradient id="officeTone" x1="0" y1="0" x2="0" y2="1"><stop offset="0" stop-color="#e4e9ef"/><stop offset="1" stop-color="#b7c3d1"/></linearGradient></defs>
      <path d="M0,480 Q170,410 380,440 L380,760 L0,760Z" fill="url(#officeTone)"/>
      <path d="M0,480 Q170,410 380,440" fill="none" stroke="var(--royal)" stroke-width="2"/>
    </svg>
    <div class="efficiency__column">
      <header class="efficiency__head">
        <h2 class="heading"><span class="heading__light">Experience</span><br><span class="heading__bold">High-Tech Efficiency</span></h2>
        <div class="rule"></div>
      </header>
      <div class="efficiency__text body">
        <p>Bluegrass Summit Building Care follows a technology-based service delivery process. In our company, employees communicate with each other using smartphone/tablet apps so that they can track every cleaning team's whereabouts.</p>
        <p>This enables main office managers to efficiently monitor work progress in real time. With this high-tech infrastructure in place, our cleaners can be able to relay on-the-spot customer requests to us immediately. We can then issue instructions just as quickly to employees on site.</p>
      </div>
    </div>
  </section>

  <section class="panel panel--services">
    <header class="services__head">
      <h2 class="heading"><span>Services</span> <b>We Offer</b></h2>
      <div class="rule"></div>
    </header>
    <p class="services__intro">Our company specializes in cleaning medical facilities and class-A office spaces. You can contact us to request:</p>
    <ul class="service-list">
      <li><svg width="16" height="16" viewBox="0 0 16 16"><circle cx="8" cy="8" r="7" fill="none" stroke="#fff" stroke-width="1.4"/><path d="M4.5 8.2l2.3 2.3 4.7-4.7" fill="none" stroke="#fff" stroke-width="1.5"/></svg><span><strong>Carpet Cleaning</strong></span></li>
      <li><svg width="16" height="16" viewBox="0 0 16 16"><circle cx="8" cy="8" r="7" fill="none" stroke="#fff" stroke-width="1.4"/><path d="M4.5 8.2l2.3 2.3 4.7-4.7" fill="none" stroke="#fff" stroke-width="1.5"/></svg><span><strong>Floor Care</strong> (Personalized Programs, Including Stripping and Waxing)</span></li>
      <li><svg width="16" height="16" viewBox="0 0 16 16"><circle cx="8" cy="8" r="7" fill="none" stroke="#fff" stroke-width="1.4"/><path d="M4.5 8.2l2.3 2.3 4.7-4.7" fill="none" stroke="#fff" stroke-width="1.5"/></svg><span><strong>Janitorial Services</strong></span></li>
      <li><svg width="16" height="16" viewBox="0 0 16 16"><circle cx="8" cy="8" r="7" fill="none" stroke="#fff" stroke-width="1.4"/><path d="M4.5 8.2l2.3 2.3 4.7-4.7" fill="none" stroke="#fff" stroke-width="1.5"/></svg><span><strong>Window Cleaning</strong></span></li>
      <li><svg width="16" height="16" viewBox="0 0 16 16"><circle cx="8" cy="8" r="7" fill="none" stroke="#fff" stroke-width="1.4"/><path d="M4.5 8.2l2.3 2.3 4.7-4.7" fill="none" stroke="#fff" stroke-width="1.5"/></svg><span><strong>24-Hour Emergency Water Extraction Services</strong></span></li>
    </ul>
    <div class="call-banner">
      <div class="call-banner__label">Call us for <b>Supplies</b></div>
      <div class="call-banner__phone">1-866-555-0142</div>
    </div>
  </section>

  <section class="panel panel--vision">
    <header class="vision__head">
      <h2 class="heading"><span class="heading__light">Our</span> <span class="heading__bold">Vision</span></h2>
      <div class="rule"></div>
    </header>
    <div class="vision__text body">
      <p>Bluegrass Summit Building Care will be one of the top independently owned commercial cleaning services, serving the central and eastern part of Kentucky.</p>
      <p>Our vision is to become the leader in commercial cleaning and building services industry by using modern technology to blaze the trail that others will follow when it comes to providing quality services and exceptional customer service.</p>
      <p>We will be relentless in our commitment to fulfill our vision and offer our clients personalized service.</p>
    </div>
    <header class="values__head">
      <h2 class="heading"><span class="heading__light">Our</span> <span class="heading__bold">Core Values</span></h2>
      <div class="rule"></div>
    </header>
    <ul class="value-list">
      <li class="value">
        <span class="value__icon"><svg width="34" height="34" viewBox="0 0 34 34" fill="none" stroke="var(--royal)" stroke-width="2"><path d="M8 15a9 9 0 0 1 16-5"/><path d="M24 5v5h-5"/><path d="M26 19a9 9 0 0 1-16 5"/><path d="M10 29v-5h5"/></svg></span>
        <span class="value__divider"></span>
        <span><span class="value__title">Consistency</span><br><span class="value__text">If you say it, mean it. If you mean it, do it.</span></span>
      </li>
      <li class="value">
        <span class="value__icon"><svg width="34" height="34" viewBox="0 0 34 34" fill="none" stroke="var(--royal)" stroke-width="2"><path d="M17 20s-7-4.5-7-9a3.5 3.5 0 0 1 7-1 3.5 3.5 0 0 1 7 1c0 4.5-7 9-7 9z"/><path d="M4 20l6 8h8M30 20l-6 8h-6"/></svg></span>
        <span class="value__divider"></span>
        <span><span class="value__title">Kindness</span><br><span class="value__text">Be the reason someone believes in the goodness of people.</span></span>
      </li>
      <li class="value">
        <span class="value__icon"><svg width="34" height="34" viewBox="0 0 34 34" fill="none" stroke="var(--royal)" stroke-width="2"><path d="M17 5v23M10 28h14M7 10h20"/><path d="M7 10l-4 9h8zM27 10l-4 9h8z"/></svg></span>
        <span class="value__divider"></span>
        <span><span class="value__title">Balance</span><br><span class="value__text">Give proper weight to every area of one's life.</span></span>
      </li>
      <li class="value">
        <span class="value__icon"><svg width="34" height="34" viewBox="0 0 34 34" fill="none" stroke="var(--royal)" stroke-width="2"><circle cx="17" cy="14" r="7"/><path d="M14 21v4h6v-4M15 28h4M17 3v2M6 14h2M26 14h2"/></svg></span>
        <span class="value__divider"></span>
        <span><span class="value__title">Motivation</span><br><span class="value__text">Empower our team to be a part of something bigger.</span></span>
      </li>
    </ul>
  </section>

  <span class="bubble bubble--lav" style="left:205px;top:418px;width:40px;height:40px"></span>
  <span class="bubble bubble--lav" style="left:258px;top:408px;width:70px;height:70px"></span>
  <span class="bubble bubble--pale" style="left:660px;top:370px;width:56px;height:56px"></span>
  <span class="bubble bubble--pale" style="left:622px;top:390px;width:26px;height:26px"></span>
  <div class="photo-circle photo-circle--team" role="img" aria-label="Photo of a smiling cleaning team in blue vests standing beside a janitorial cart"></div>
  <div class="photo-circle photo-circle--supplies" role="img" aria-label="Photo of a blue bucket filled with cleaning supplies and dusters"></div>
</main>
</body>
</html>
```